Lumora business card for a plastic surgeon

we need a business card for plastic surgeons that work on a clinic called LUMORA.
we want a clean design and the following informations: name of the doctor, doctor's registration number (called CRM), telephone, address, facebook, instagram.
Colors: white, blue tones, light brown/ coffee

facebook and instagram: lumoracirurgiaestetica

Industry/Entity Type

Business

Contact Information for Business Card

clean design

Font styles to use
Serif
Sans Serif
Other font styles liked:
• helvetica light

Colors
cee9f5
85cae6
85abd2
3276b5
cfeae6
cedeed
eaf1f7

Requirements
Must have
• doctor's name
• identification number (called CRM)
• contact (phone, facebook, instagram, address)

```html
<!DOCTYPE html>
<html lang="pt">
<head>
<meta charset="utf-8">
<title>Lumora Cirurgia Plástica – Business Card</title>
<link rel="stylesheet" href="https://fonts.googleapis.com/css2?family=Marcellus&family=Open+Sans:wght@300;400&display=swap">
<style>
  :root {
    --page: #ececec;
    --card: #ffffff;
    --cyan: #29b6d6;
    --navy: #1b3a63;
    --blue-top: #1f9ac0;
    --blue-bottom: #1b4f80;
    --text-light: #ffffff;
    --rule: rgba(255,255,255,0.75);
  }
  * { margin: 0; padding: 0; box-sizing: border-box; }
  html, body {
    width: 1200px; height: 1200px; overflow: hidden;
    background: var(--page);
    font-family: "Open Sans", Arial, sans-serif;
  }
  .canvas { position: relative; width: 1200px; height: 1200px; }

  .card {
    position: absolute;
    width: 520px; height: 300px;
    background: var(--card);
    box-shadow: 0 14px 30px rgba(0,0,0,0.18);
    overflow: hidden;
  }
  .card--back { left: 50px; top: 200px; }
  .card--front { left: 630px; top: 200px; }

  .card__panel { position: absolute; inset: 0; }

  .contact {
    position: absolute; left: 30px; top: 34px; width: 200px;
    color: var(--text-light); font-weight: 300;
  }
  .contact__name { font-size: 26px; font-weight: 300; letter-spacing: 0.5px; }
  .contact__crm { font-size: 13px; margin-top: 2px; }
  .contact__phone { font-size: 15px; margin-top: 26px; }
  .contact__rule { border: 0; border-top: 1px solid var(--rule); width: 190px; margin: 8px 0 10px; }
  .contact__address { font-size: 14px; line-height: 1.45; }

  .wordmark { text-align: center; }
  .wordmark__name {
    font-family: "Marcellus", "Times New Roman", serif;
    color: var(--cyan); letter-spacing: 4px; line-height: 1;
  }
  .wordmark__tagline {
    font-family: "Marcellus", "Times New Roman", serif;
    color: var(--navy); letter-spacing: 2px;
  }

  .card--back .wordmark { position: absolute; left: 248px; top: 78px; width: 250px; }
  .card--back .wordmark__name { font-size: 54px; }
  .card--back .wordmark__tagline { font-size: 17px; margin-top: 6px; }

  .social {
    position: absolute; right: 24px; bottom: 22px;
    display: flex; align-items: center; gap: 8px;
    color: var(--navy); font-size: 14px;
  }
  .social__dot { width: 16px; height: 16px; border-radius: 50%; background: var(--blue-bottom); }

  .card--front .wordmark { position: absolute; left: 0; right: 0; top: 92px; }
  .card--front .wordmark__name { font-size: 76px; }
  .card--front .wordmark__tagline { font-size: 24px; margin-top: 8px; }

  .signature-logo { position: absolute; left: 640px; top: 820px; width: 500px; }
  .signature-logo .wordmark__name { font-size: 96px; letter-spacing: 6px; }
  .signature-logo .wordmark__tagline { font-size: 34px; margin-top: 14px; }
</style>
</head>
<body>
<main class="canvas">

  <section class="card card--back" aria-label="Verso do cartão">
    <svg class="card__panel" viewBox="0 0 520 300" width="520" height="300" aria-hidden="true">
      <defs>
        <linearGradient id="panelBlue" x1="0" y1="0" x2="0" y2="1">
          <stop offset="0" stop-color="#1f9ac0"/>
          <stop offset="1" stop-color="#1b4f80"/>
        </linearGradient>
      </defs>
      <path d="M0 0 H270 C235 90 225 200 248 300 H0 Z" fill="url(#panelBlue)"/>
      <path d="M270 0 C235 90 225 200 248 300" fill="none" stroke="#29b6d6" stroke-width="5"/>
      <path d="M278 0 C244 90 234 200 257 300" fill="none" stroke="#e6eef3" stroke-width="5"/>
    </svg>

    <div class="contact">
      <p class="contact__name">JOHN DOE</p>
      <p class="contact__crm">CRM</p>
      <p class="contact__phone">Tel. 1-234-567890</p>
      <hr class="contact__rule">
      <p class="contact__address">Dummy city<br>Dummy Country Land Dummy</p>
    </div>

    <div class="wordmark">
      <p class="wordmark__name">LUMORA</p>
      <p class="wordmark__tagline">CIRURGIA PLÁSTICA</p>
    </div>

    <div class="social">
      <span class="social__dot"></span>
      <span class="social__handle">lumoracirurgiaestetica</span>
    </div>
  </section>

  <section class="card card--front" aria-label="Frente do cartão">
    <div class="wordmark">
      <p class="wordmark__name">LUMORA</p>
      <p class="wordmark__tagline">CIRURGIA PLÁSTICA</p>
    </div>
  </section>

  <div class="signature-logo wordmark">
    <p class="wordmark__name">LUMORA</p>
    <p class="wordmark__tagline">CIRURGIA PLÁSTICA</p>
  </div>

</main>
</body>
</html>
```